Women's Jewellery startup needs a captivating, beautifully designed and intuitive online store

[12/24 update]

Added 2 additional documents:

Feedback on designs received so far: designer feedback.docx
Product images from catalogue: products images.docx

Please read the feedback provided on designs provided so far to guide you further on your submission. The product images can be used to create promotional banners for the site.

@@@Added a document (VELISSE JEWELLERY_checklist.docx) which can be used by designers as a checklist when submitting their designs to ensure all aspects of the requirements have been covered @@@

+++IMPORTANT BUT NOT SPECIFIED IN THE REQUIREMENTS DOCUMENT - DESIGN SHOULD INCLUDE SUPPORT FOR MOBILE FRIENDLY SITE TOO+++

***Previous experience designing Jewellery online stores preferred (not essential)***

The name of the online Jewellery store is "Velisse Jewellery" and the business is based in Hong Kong. It will be run by 2 stay at home mothers. We need a Shopify themed store designed that will achieve the following objectives in order of priority:

• Conversion: The primary objective of the design/content is to prompt the customer to make a purchase. While this may sound obvious, it is mentioned so as not to distract the design process by focusing on other objectives (which are also important). The site also needs to be optimized so as to rank high in search engine searches for relevant keywords (SEO)
• Navigation: An intuitive interface which takes away a lot of the thinking from the customer by making it obvious what they need to do when they visit the store
• Engagement: Encourages the customer to spend time on the website and share content with their social network

Where applicable, the design of the store should reflect as closely as possible the mission statements and words outlined below:

• Jewellery you’ll fall in love with
• We want every client to leave the store with a smile
• We want to be able to provide the best service we can in every situation no matter what
• We aim to increase our business by word of mouth; therefore we tell people things about our store that makes it interesting for them to share
• We love every customer, no matter how difficult things get
• We, as a team, are so well informed about our products and brands that we always have the best information for our customers
• We celebrate women here!
• We celebrate life in here!
• We celebrate beauty here!
• We celebrate families here, as jewellery often stays within families.
• We will always try to make an extra step
• We will always try to exceed the expectation of our customers
• We will go as far as we possibly can to attract a customer back to our store and connect with us
• Every client that leaves our store knows more about jewellery because we passionately told him about it
• Romantic, classic, love, warm, cool, stylish

A draft functional specification is attached with this brief. We would like the design to reflect as closely as possible the functional requirements outlined in the document. Open to suggestions to improve upon the functional requirements.

Target Market(s)

Women aged 18-55

Industry/Entity Type

Jewelry Store

Coding

Coded - Design and coding required

Number of Pages Required

5+ page

Font styles to use
Other font styles liked:
• Myriad Pro as per Logo but open to any font that complements this one

Requirements
Must have
• 1. A look that encourages the user to make a purchase
• 2. An intuitive, easy to navigate and engaging interface
• 3. Primary colour scheme as defined in the functional specification attached
• 4. Simplistic look, not too cluttered
Nice to have
• 1. Closely matching the functional requirements of the site as outlined in the requirements specification but open to any better ideas

```html
<!DOCTYPE html>
<html lang="en">
<head>
<meta charset="utf-8">
<title>Velisse Jewellery – Home</title>
<link href="https://fonts.googleapis.com/css2?family=Josefin+Sans:wght@600;700&family=PT+Sans:ital,wght@0,400;0,700;1,400&family=PT+Sans+Narrow:wght@700&display=swap" rel="stylesheet">
<style>
:root{
  --gold:#c9a05a;
  --gold-dark:#b88a3e;
  --ink:#1b1b1b;
  --grey-tile:#b9b9b9;
  --line:#d6d6d6;
  --footer:#1c1c1c;
  --stage:#efefef;
  --muted:#777;
}
*{box-sizing:border-box;margin:0;padding:0}
html,body{width:959px;height:1200px;overflow:hidden;background:var(--stage)}
body{font-family:"PT Sans",sans-serif;color:var(--ink)}
.stage{position:absolute;left:0;top:0;width:1199px;height:1500px;transform:scale(.8);transform-origin:0 0}

/* ---------- desktop page ---------- */
.desktop{position:absolute;left:30px;top:85px;width:760px;height:1385px;background:#fff;box-shadow:0 6px 24px rgba(0,0,0,.18);overflow:hidden}
.topbar{position:absolute;left:0;top:0;width:760px;height:22px;border-bottom:1px solid var(--line);font-size:7px;line-height:22px}
.topbar .currency{position:absolute;left:127px}
.offer{color:var(--gold-dark)}
.topbar .offer{position:absolute;left:202px}
.topbar .tools{position:absolute;right:126px;top:0;display:flex;align-items:center;gap:7px;height:22px}
.tools svg{display:block}
.brand{position:absolute;left:0;top:22px;width:760px;height:82px;display:flex;flex-direction:column;align-items:center;justify-content:center;gap:8px}
.brand .mark{width:30px;height:30px;border:1.5px solid var(--gold);border-radius:50%}
.brand .name{font-size:12px;letter-spacing:5px;color:var(--gold-dark)}

/* photo placeholders: flat tonal fields filling the whole frame */
.hero{position:absolute;left:0;top:104px;width:760px;height:352px;background:#000;overflow:hidden}
.hero .photo,.m-hero .photo{position:absolute;inset:0;
  background:
    linear-gradient(160deg,rgba(0,0,0,0) 0%,rgba(0,0,0,0) 30%,rgba(190,190,190,.35) 42%,rgba(0,0,0,0) 56%),
    linear-gradient(100deg,#070707 0%,#3c3c3c 25%,#6d6d6d 45%,#2c2c2c 62%,#8a8a8a 78%,#111 100%);}
.hero .photo::after,.m-hero .photo::after{content:"";position:absolute;inset:0;background:linear-gradient(180deg,rgba(0,0,0,.15),rgba(0,0,0,.35) 60%,rgba(0,0,0,.85))}
.hero h1{position:absolute;left:0;width:760px;top:118px;text-align:center;font-family:"PT Sans Narrow",sans-serif;font-weight:700;font-size:31px;color:#fff;letter-spacing:-.3px;text-shadow:0 1px 3px rgba(0,0,0,.6)}
.hero .bar{position:absolute;left:631px;top:122px;width:1.5px;height:28px;background:#fff}
.hero p{position:absolute;left:0;width:760px;top:163px;text-align:center;font-size:9.5px;color:#eee}
.hero .cta{position:absolute;left:0;width:760px;top:192px;text-align:center;font-size:9.5px;font-weight:700;color:#fff}
.dots{position:absolute;display:flex;gap:2px}
.dots i{display:block;width:5px;height:5px;background:var(--gold)}
.dots i:first-child{background:#fff}
.hero .dots{left:371px;top:258px}

.tile{position:absolute;width:162px;height:141px;background:var(--grey-tile);overflow:hidden}
.tile .photo{position:absolute;inset:0;clip-path:polygon(100% 0,100% 100%,0 100%)}
.tile h3{position:absolute;font-weight:700;font-size:10.5px;color:#111;z-index:1}
.tile .sub{position:absolute;font-size:6.5px;color:#222;z-index:1}
.tile .btn{position:absolute;border:1px solid #333;border-radius:3px;font-size:5.5px;font-weight:700;height:16px;line-height:14px;padding:0 9px;color:#111;background:rgba(255,255,255,.15);z-index:1}
.ph-ruby{background:linear-gradient(150deg,#2e2220 0%,#4a3431 35%,#1c1515 55%,#9c7468 78%,#d9b2a4 100%)}
.ph-aqua{background:linear-gradient(150deg,#1a1a1a 0%,#050505 50%,#6b5228 75%,#c59a4c 100%)}
.ph-diamond{background:linear-gradient(150deg,#9a9a9a 0%,#e6e6e6 35%,#7a7a7a 55%,#cfcfcf 70%,#1b1b1b 100%)}

.section-title{position:absolute;text-align:center;font-family:"Josefin Sans",sans-serif;font-weight:700;color:#222;letter-spacing:.5px}
.section-title b{color:var(--gold);font-weight:700}
.section-sub{position:absolute;text-align:center;color:var(--muted)}

.card{position:absolute;width:116px;height:214px;border:1px solid #e2c99d;background:#fff;text-align:center}
.card .shot{position:absolute;left:3px;top:0;right:3px;height:150px;border:1px solid #eee;box-shadow:0 1px 3px rgba(0,0,0,.12);background:#fff;padding:8px}
.card .shot span{display:block;width:100%;height:100%}
.pr-ring{background:linear-gradient(135deg,#fafafa 0%,#d9d3e6 30%,#b8d8d3 50%,#c9c9c9 70%,#fafafa 100%)}
.pr-bracelet{background:linear-gradient(135deg,#fafafa 0%,#f0dcae 30%,#c79a3a 48%,#8a2a20 58%,#f0dcae 75%,#fafafa 100%)}
.pr-earring{background:linear-gradient(90deg,#fafafa 0%,#d4d4d4 25%,#3a3a3a 35%,#e8e8e8 50%,#3a3a3a 65%,#d4d4d4 75%,#fafafa 100%)}
.pr-necklace{background:linear-gradient(180deg,#fafafa 0%,#e3e3e3 40%,#7e88c9 65%,#e8eaf4 85%,#fafafa 100%)}
.card .type{position:absolute;left:0;right:0;top:162px;font-size:7.5px;font-weight:700}
.card .metal{position:absolute;left:0;right:0;top:175px;font-size:6.5px;font-style:italic;color:#555}
.card .price{position:absolute;left:0;right:0;top:192px;font-size:8px;color:var(--gold-dark)}
.arrow-btn{position:absolute;width:22px;height:22px;border-radius:50%;background:#cfcfcf;display:flex;align-items:center;justify-content:center}

.newsletter{position:absolute;left:127px;top:1005px;width:507px;height:43px;border-top:1px solid #aaa;border-bottom:1px solid #aaa}
.newsletter .thumb{position:absolute;left:0;top:2px;width:42px;height:38px;background:linear-gradient(135deg,#f4f4f4,#c8c8c8 50%,#ececec)}
.newsletter h4{position:absolute;left:86px;top:15px;font-family:"Josefin Sans",sans-serif;font-size:10.5px;letter-spacing:.6px;color:#222}
.newsletter h4 b{color:var(--gold)}
.newsletter .divider{position:absolute;left:252px;top:3px;width:2px;height:36px;background:var(--gold)}
.newsletter .field{position:absolute;left:269px;top:16px;display:flex;align-items:center;gap:8px;font-size:6.5px;color:var(--gold-dark)}
.newsletter .go{position:absolute;right:30px;top:18px}

.footer{position:absolute;left:0;top:1088px;width:760px;height:297px;background:var(--footer);color:#fff}
.footer .map{position:absolute;left:170px;top:30px;width:420px;height:240px;background:linear-gradient(180deg,#262626,#232323 50%,#1f1f1f)}
.footer h4{position:absolute;left:0;width:760px;top:37px;text-align:center;font-family:"Josefin Sans",sans-serif;font-size:11px;letter-spacing:.5px}
.footer h4 b{color:var(--gold)}
.ff{position:absolute;border-bottom:1px solid #bbb;font-size:6px;height:10px}
.submit{position:absolute;left:345px;top:132px;width:71px;height:20px;background:var(--gold);font-size:7px;font-weight:700;text-align:center;line-height:20px}
.footer .rule{position:absolute;left:0;top:173px;width:760px;height:1px;background:#3a3a3a}
.fcol{position:absolute;top:190px;font-size:6.5px;line-height:15px}
.fcol h5{font-size:9px;font-weight:400;margin-bottom:6px;line-height:12px}
.fcopy{position:absolute;left:499px;top:196px;font-size:6.5px;line-height:13px}
.social{position:absolute;left:499px;top:250px;display:flex;gap:8px}
.social i{display:block;width:20px;height:20px;border:1px solid #ccc;border-radius:50%}

/* ---------- mobile page ---------- */
.mobile{position:absolute;left:861px;top:166px;width:286px;height:1334px;background:#fff;border:2px solid #222;border-bottom:none;overflow:hidden}
.m-top{position:absolute;left:0;top:0;width:282px;height:21px;border-bottom:1px solid var(--line);font-size:6px;line-height:21px}
.m-top .offer{position:absolute;left:10px}
.m-top .tools{position:absolute;right:6px;top:0;display:flex;gap:5px;align-items:center;height:21px}
.m-brand{position:absolute;left:0;top:21px;width:282px;height:48px;display:flex;flex-direction:column;align-items:center;justify-content:center;gap:4px}
.m-brand .mark{width:16px;height:16px;border:1px solid var(--gold);border-radius:50%}
.m-brand .name{font-size:6.5px;letter-spacing:3px;color:var(--gold-dark)}
.m-hero{position:absolute;left:0;top:69px;width:282px;height:256px;background:#000;overflow:hidden}
.m-hero h2{position:absolute;left:0;width:282px;top:100px;text-align:center;font-family:"PT Sans Narrow",sans-serif;font-weight:700;font-size:15.5px;color:#fff;text-shadow:0 1px 2px rgba(0,0,0,.6)}
.m-hero p{position:absolute;left:0;width:282px;top:121px;text-align:center;font-size:4.5px;color:#ddd}
.m-hero .cta{position:absolute;left:0;width:282px;top:134px;text-align:center;font-size:4.5px;font-weight:700;color:#fff}
.m-hero .dots{left:135px;top:169px}
.m-hero .dots i{width:3px;height:3px}
.mtile{width:217px;height:187px}
.mtile h3{font-size:12px}
.mtile .sub{font-size:9px}
.mtile .btn{font-size:7px;height:23px;line-height:21px;padding:0 10px}
.mcard{width:132px;height:249px}
.mcard .shot{height:176px}
.mcard .type{top:189px;font-size:9px}
.mcard .metal{top:204px;font-size:8px}
.mcard .price{top:223px;font-size:9.5px}
</style>
</head>
<body>
<div class="stage">

  <main class="desktop">
    <div class="topbar">
      <span class="currency">Currency Selector $</span>
      <span class="offer">Extra 10% off Diamond rings till March 31st, 2018</span>
      <div class="tools">
        <span style="display:flex;align-items:center;gap:3px">
          <svg width="7" height="8" viewBox="0 0 7 8"><circle cx="3.5" cy="2" r="2" fill="#222"/><path d="M0 8c0-3 7-3 7 0z" fill="#222"/></svg>Sign Up</span>
        <svg width="8" height="7" viewBox="0 0 8 7"><path d="M4 7L0.6 3.4A1.9 1.9 0 0 1 4 1a1.9 1.9 0 0 1 3.4 2.4z" fill="#222"/></svg>
        <svg width="10" height="8" viewBox="0 0 10 8"><path d="M0 .5h2l1.3 5h5L9.5 2H2.6" fill="none" stroke="#222" stroke-width="1"/><circle cx="4" cy="7.2" r=".8" fill="#222"/><circle cx="7.5" cy="7.2" r=".8" fill="#222"/></svg>
        <svg width="8" height="8" viewBox="0 0 8 8"><circle cx="3.3" cy="3.3" r="2.5" fill="none" stroke="#222" stroke-width="1"/><path d="M5.2 5.2L7.6 7.6" stroke="#222" stroke-width="1.2"/></svg>
      </div>
    </div>

    <header class="brand">
      <span class="mark"></span>
      <span class="name">VELISSE</span>
    </header>

    <section class="hero">
      <div class="photo" role="img" aria-label="Close-up of two silver diamond rings on black"></div>
      <h1>EVERY PIECE OF JEWELRY TELLS A STORY</h1>
      <span class="bar"></span>
      <p>Be real be yourself, carry a piece of natural and real jewelry</p>
      <div class="cta">LEARN MORE →</div>
      <div class="dots"><i></i><i></i><i></i></div>
    </section>

    <section class="categories">
      <article class="tile" style="left:127px;top:506px">
        <div class="photo ph-ruby" role="img" aria-label="Rose gold ruby ring"></div>
        <h3 style="left:32px;top:12px">RUBY</h3>
        <span class="sub" style="left:24px;top:27px">10K Rose Gold</span>
        <span class="btn" style="left:11px;top:46px">VIEW COLLECTION</span>
      </article>
      <article class="tile" style="left:299px;top:506px">
        <div class="photo ph-aqua" role="img" aria-label="Gold aquamarine necklace pendant"></div>
        <h3 style="left:11px;top:12px">AQUAMARINE</h3>
        <span class="sub" style="left:24px;top:27px">10K Rose Gold</span>
        <span class="btn" style="left:15px;top:46px">SHOP NECKLACE</span>
      </article>
      <article class="tile" style="left:472px;top:506px">
        <div class="photo ph-diamond" role="img" aria-label="Sparkling diamond jewellery"></div>
        <h3 style="left:20px;top:12px">DIAMOND</h3>
        <span class="sub" style="left:24px;top:27px">10K Rose Gold</span>
        <span class="btn" style="left:11px;top:46px;padding:0 19px">SHOP NOW</span>
      </article>
    </section>

    <h2 class="section-title" style="left:0;width:760px;top:687px;font-size:18px">OUR P<b>RO</b>DUCT</h2>
    <p class="section-sub" style="left:0;width:760px;top:711px;font-size:8px">Trending &amp; stunning. Unique.</p>

    <section class="products">
      <span class="arrow-btn" style="left:94px;top:849px"><svg width="8" height="6" viewBox="0 0 8 6"><path d="M8 3H1M3 .5L.7 3 3 5.5" fill="none" stroke="#333" stroke-width="1"/></svg></span>
      <article class="card" style="left:127px;top:750px">
        <div class="shot"><span class="pr-ring" role="img" aria-label="Silver ring set with multi-coloured gemstones"></span></div>
        <div class="type">RING</div><div class="metal">10K Rose Gold</div><div class="price">$220.00 - $349.00</div>
      </article>
      <article class="card" style="left:258px;top:750px">
        <div class="shot"><span class="pr-bracelet" role="img" aria-label="Gold ring with red garnet stones"></span></div>
        <div class="type">BRACELET</div><div class="metal">14K Gold Rose</div><div class="price">$220.00 - $349.00</div>
      </article>
      <article class="card" style="left:388px;top:750px">
        <div class="shot"><span class="pr-earring" role="img" aria-label="Pair of silver drop earrings with dark stones"></span></div>
        <div class="type">EARRING</div><div class="metal">10K Yellow Gold</div><div class="price">$220.00 - $349.00</div>
      </article>
      <article class="card" style="left:518px;top:750px">
        <div class="shot"><span class="pr-necklace" role="img" aria-label="Silver chain necklace with blue sapphire pendant"></span></div>
        <div class="type">NECKLACES</div><div class="metal">Gold plated</div><div class="price">$220.00 - $349.00</div>
      </article>
      <span class="arrow-btn" style="left:644px;top:849px"><svg width="8" height="6" viewBox="0 0 8 6"><path d="M0 3h7M5 .5L7.3 3 5 5.5" fill="none" stroke="#333" stroke-width="1"/></svg></span>
    </section>

    <section class="newsletter">
      <div class="thumb" role="img" aria-label="Silver engagement ring"></div>
      <h4>SIGNUP <b>FOR</b> NEWSLETTER</h4>
      <span class="divider"></span>
      <div class="field">
        <svg width="11" height="8" viewBox="0 0 11 8"><rect x=".5" y=".5" width="10" height="7" fill="none" stroke="#c9a05a"/><path d="M.5 .5l5 4 5-4" fill="none" stroke="#c9a05a"/></svg>
        Enter Your E-mail Address
      </div>
      <svg class="go" width="9" height="7" viewBox="0 0 9 7"><path d="M0 3.5h8M5.5 1L8 3.5 5.5 6" fill="none" stroke="#b88a3e" stroke-width="1"/></svg>
    </section>

    <footer class="footer">
      <div class="map" role="img" aria-label="Dotted world map"></div>
      <h4>KEEP <b>IN</b> TOUCH</h4>
      <span class="ff" style="left:127px;top:64px;width:163px">NAME</span>
      <span class="ff" style="left:318px;top:64px;width:133px">E-MAIL</span>
      <span class="ff" style="left:496px;top:64px;width:138px">PHONE</span>
      <span class="ff" style="left:127px;top:91px;width:507px">MESSAGE</span>
      <span class="submit">SUBMIT</span>
      <span class="rule"></span>
      <div class="fcol" style="left:127px"><h5>About Us</h5>Our Story<br>Wholesale inquiries</div>
      <div class="fcol" style="left:257px"><h5>Shopping</h5>Orders<br>Wishlist<br>Size Guide</div>
      <div class="fcol" style="left:367px"><h5>Customer Care</h5>Returns<br>FAQ's<br>Care &amp; Warranty<br>Contact Us</div>
      <div class="fcopy">© Copyright 2017 Velisse Jewellery.<br>All Rights Reserved.<br><span style="display:block;margin-top:4px">Privacy &nbsp;Policy . Terms and Conditions</span></div>
      <div class="social"><i></i><i></i><i></i></div>
    </footer>
  </main>

  <main class="mobile">
    <div class="m-top">
      <span class="offer">Extra 10% off Diamond rings till March 31st, 2018</span>
      <div class="tools">
        <svg width="8" height="7" viewBox="0 0 8 7"><path d="M4 7L0.6 3.4A1.9 1.9 0 0 1 4 1a1.9 1.9 0 0 1 3.4 2.4z" fill="#222"/></svg>
        <svg width="10" height="8" viewBox="0 0 10 8"><path d="M0 .5h2l1.3 5h5L9.5 2H2.6" fill="none" stroke="#222"/><circle cx="4" cy="7.2" r=".8" fill="#222"/><circle cx="7.5" cy="7.2" r=".8" fill="#222"/></svg>
        <svg width="8" height="8" viewBox="0 0 8 8"><circle cx="3.3" cy="3.3" r="2.5" fill="none" stroke="#222"/><path d="M5.2 5.2L7.6 7.6" stroke="#222" stroke-width="1.2"/></svg>
      </div>
    </div>
    <header class="m-brand"><span class="mark"></span><span class="name">VELISSE</span></header>
    <section class="m-hero">
      <div class="photo" role="img" aria-label="Close-up of two silver diamond rings on black"></div>
      <h2>EVERY PIECE OF JEWELRY TELLS A STORY</h2>
      <p>Be real be yourself, carry a piece of natural and real jewelry</p>
      <div class="cta">LEARN MORE →</div>
      <div class="dots"><i></i><i></i><i></i></div>
    </section>

    <article class="tile mtile" style="left:31px;top:377px">
      <div class="photo ph-ruby" role="img" aria-label="Rose gold ruby ring"></div>
      <h3 style="left:46px;top:16px">RUBY</h3>
      <span class="sub" style="left:32px;top:35px">10K Rose Gold</span>
      <span class="btn" style="left:19px;top:62px">VIEW COLLECTION</span>
    </article>
    <article class="tile mtile" style="left:31px;top:575px">
      <div class="photo ph-aqua" role="img" aria-label="Gold aquamarine necklace pendant"></div>
      <h3 style="left:23px;top:16px">AQUAMARINE</h3>
      <span class="sub" style="left:32px;top:35px">10K Rose Gold</span>
      <span class="btn" style="left:19px;top:62px">SHOP NECKLACE</span>
    </article>
    <article class="tile mtile" style="left:31px;top:773px">
      <div class="photo ph-diamond" role="img" aria-label="Sparkling diamond jewellery"></div>
      <h3 style="left:33px;top:16px">DIAMOND</h3>
      <span class="sub" style="left:32px;top:35px">10K Rose Gold</span>
      <span class="btn" style="left:19px;top:62px;padding:0 22px">SHOP NOW</span>
    </article>

    <h2 class="section-title" style="left:0;width:282px;top:998px;font-size:15px">OUR P<b>RO</b>DUCT</h2>
    <p class="section-sub" style="left:0;width:282px;top:1019px;font-size:7.5px">Trending &amp; stunning. Unique.</p>

    <article class="card mcard" style="left:72px;top:1048px">
      <div class="shot"><span class="pr-ring" role="img" aria-label="Silver ring set with multi-coloured gemstones"></span></div>
      <div class="type">RING</div><div class="metal">10K Rose Gold</div><div class="price">$220.00 - $349.00</div>
    </article>
    <article class="card mcard" style="left:72px;top:1312px"></article>
  </main>

</div>
</body>
</html>
```